Calder Mindworks Psychology website transfer from WIX to Wordpress

I have a website currently coded in WIX and I want it (or something like it or better) designed to be coded on Wordpress instead. The website should have mobile optimization so that it can be viewed on mobile devices.

The current website is at: www.caldermindworks.example

I'm not looking for versions of the website that are very different to what I already have, unless they improve on it aesthetically. I'm mainly looking to have a Wordpress version of this website that I built, away from the WIX ecosystem.

Target Market(s)

Psychology services clients

Coding

Coded - Design and coding required

Number of Pages Required

5+ page

Font styles to use
Serif

Requirements
Must have
• The finished product shoud match my website exactly.
Nice to have
• I'm happy to see new ideas that improve on the current website.
Should not have
• It should not be a different version of my website.

```html
<!DOCTYPE html>
<html lang="en">
<head>
<meta charset="utf-8">
<title>Calder Mindworks Psychology</title>
<link rel="stylesheet" href="https://fonts.googleapis.com/css2?family=Ubuntu:wght@400;500;700&family=Open+Sans:wght@400;600&display=swap">
<style>
:root{
  --green:#284a3f;
  --green-dark:#1e3a31;
  --navy:#101a35;
  --footer:#0d1430;
  --ink:#1b2236;
  --muted:#7a8190;
  --light:#f5f5f5;
  --white:#ffffff;
}
*{box-sizing:border-box;margin:0;padding:0}
html,body{width:1200px;height:4186px;overflow:hidden;background:var(--white)}
body{position:relative;font-family:"Open Sans",sans-serif;color:var(--ink)}
.abs{position:absolute}
.head-font{font-family:"Ubuntu",sans-serif}
.topbar{left:488px;top:0;width:712px;height:32px;background:var(--green);clip-path:polygon(0 0,100% 0,100% 100%,22px 100%);color:#fff;font-size:12px;font-weight:600}
.topbar span{position:absolute;top:5px;display:flex;align-items:center;gap:8px}
.ic-ring{width:22px;height:22px;border:1.5px solid #fff;border-radius:50%;display:inline-flex;align-items:center;justify-content:center}
.header{left:0;top:32px;width:1200px;height:57px;background:#fff}
.brand{left:187px;top:22px;font-family:"Ubuntu",sans-serif;font-weight:500;color:var(--green);font-size:22px;line-height:1.1;display:flex;align-items:center;gap:10px}
.brand-dot{width:26px;height:26px;border-radius:50%;background:var(--green)}
.nav a{position:absolute;top:55px;font-size:12px;font-weight:600;color:var(--ink);text-decoration:none}
.nav .active{color:var(--green)}
.nav .active::after{content:"";position:absolute;left:-6px;right:-6px;top:28px;height:3px;background:var(--green)}
.soc{position:absolute;top:51px;width:22px;height:22px;border:1.5px solid #2a4fa0;border-radius:50%}
.hero-photo{left:0;top:89px;width:1200px;height:740px;background:linear-gradient(90deg,#0b0d10 0%,#2a2b2e 28%,#8a8580 55%,#d8d4cf 75%,#ebe7e2 100%)}
.hero-tag{left:122px;top:281px;width:265px;height:44px;background:#17202f;border-left:3px solid var(--green);color:#fff;font-size:21px;font-weight:700;padding:8px 0 0 20px}
.hero-title{left:116px;top:330px;color:#fff;font-size:66px;font-weight:700}
.hero-text{left:122px;top:424px;width:430px;color:#fff;font-size:17px;line-height:26px}
.btn{background:var(--green);color:#fff;font-family:"Ubuntu",sans-serif;font-weight:700;display:flex;align-items:center;justify-content:center;gap:8px}
.hero-btn{left:122px;top:524px;width:174px;height:48px;font-size:17px}
.about-photo{left:220px;top:878px;width:317px;height:455px;background:linear-gradient(180deg,#e9e9ea,#2b2d33 60%,#1a1b1f)}
.label{font-size:12px;font-weight:600;color:var(--ink);text-transform:uppercase;border-bottom:1.5px solid var(--green);padding-bottom:3px}
.h2{font-family:"Ubuntu",sans-serif;font-weight:700;color:var(--navy);font-size:39px;line-height:46px}
.p-small{font-size:12.5px;line-height:19px;color:var(--muted)}
.services{left:0;top:1333px;width:1200px;height:553px;background:linear-gradient(180deg,#2a2624,#3a332f 50%,#241f1d);clip-path:path("M0 60 Q600 -60 1200 60 L1200 553 L0 553 Z")}
.svc-card{position:absolute;background:#fff;text-align:center;padding-top:26px}
.svc-card.feature{background:var(--green);color:#fff}
.svc-icon{width:82px;height:82px;border-radius:50%;background:var(--green);margin:0 auto;display:flex;align-items:center;justify-content:center}
.feature .svc-icon{background:#fff}
.svc-card h3{font-family:"Ubuntu",sans-serif;font-size:19px;font-weight:700;color:var(--navy);margin-top:26px}
.feature h3{color:#fff}
.svc-card p{font-size:13px;line-height:21px;color:var(--muted);margin:8px auto 0;width:210px}
.feature p{color:#e6ece9}
.why-bg{left:0;top:1886px;width:1200px;height:638px;background:var(--light)}
.why-photo{left:203px;top:1927px;width:334px;height:597px;background:linear-gradient(180deg,#3a2a22 0%,#9a7a62 30%,#c9b29a 55%,#e8e3dc 100%)}
.feat{position:absolute;width:219px;height:99px;background:#fff;padding:18px 0 0 68px}
.feat svg{position:absolute;left:20px;top:22px}
.feat h4{font-family:"Ubuntu",sans-serif;font-size:16px;font-weight:500;color:#4a5566}
.feat p{font-size:12.5px;line-height:20px;color:var(--muted);margin-top:4px}
.appt{left:0;top:2524px;width:1200px;height:460px;background:linear-gradient(90deg,#1c1c1e,#2d2a28 50%,#3a3633);clip-path:path("M0 0 L1200 0 L1200 400 Q600 500 0 400 Z")}
.appt-people{left:730px;top:2478px;width:410px;height:506px;background:linear-gradient(180deg,#3b2a22,#1e2230 50%,#141826);border-radius:120px 120px 0 0}
.field{position:absolute;width:233px;height:44px;background:#fff;font-size:14px;color:#333;display:flex;align-items:center;gap:8px;padding-left:16px}
.field.tall{height:113px;align-items:flex-start;padding-top:13px}
.steps-bg{left:0;top:2984px;width:1200px;height:820px;background:var(--light)}
.step{position:absolute;width:223px;height:195px;border-radius:50%;background:#fff;text-align:center;top:3366px}
.step.feature{background:var(--green);color:#fff}
.step-icon{position:absolute;left:56px;top:-66px;width:111px;height:111px;border-radius:50%;background:var(--green);display:flex;align-items:center;justify-content:center}
.step.feature .step-icon{background:#fff}
.step-num{position:absolute;left:100px;top:40px;width:22px;height:22px;border-radius:50%;background:#fff;color:var(--green);font-size:12px;font-weight:700;line-height:22px}
.step h4{font-family:"Ubuntu",sans-serif;font-size:15px;font-weight:700;color:#2a6f8a;margin-top:75px}
.step.feature h4{color:#fff}
.step p{font-size:10px;line-height:13px;color:#333;width:180px;margin:6px auto 0}
.step.feature p{color:#e6ece9}
.step .more{font-size:9.5px;color:#2a6f8a;margin-top:8px;display:block}
.step.feature .more{color:#fff}
.footer{left:0;top:3790px;width:1200px;height:340px;background:var(--footer)}
.foot-nav a{position:absolute;top:3950px;color:#fff;font-size:15px;text-decoration:none}
.contact{position:absolute;top:4050px;color:#fff;font-size:12.5px;line-height:18px;display:flex;align-items:center;gap:14px}
.c-ring{width:56px;height:56px;border:1.5px solid #fff;border-radius:50%;display:flex;align-items:center;justify-content:center}
.bottom{left:0;top:4130px;width:1200px;height:56px;background:var(--green-dark);color:#fff;font-size:13px}
.sq{position:absolute;top:16px;width:26px;height:26px;border:1.5px solid #fff}
</style>
</head>
<body>

<div class="abs header"></div>
<div class="abs topbar">
  <span style="left:95px"><i class="ic-ring"><svg width="12" height="12" viewBox="0 0 24 24"><path d="M5 3l4 1 1 5-2 1a11 11 0 006 6l1-2 5 1 1 4-3 2C10 21 3 14 3 6z" fill="none" stroke="#fff" stroke-width="2"/></svg></i>CALL US TODAY : (555) 014-2290</span>
  <span style="left:358px"><i class="ic-ring"><svg width="12" height="12" viewBox="0 0 24 24"><rect x="3" y="6" width="18" height="12" fill="none" stroke="#fff" stroke-width="2"/><path d="M3 6l9 7 9-7" fill="none" stroke="#fff" stroke-width="2"/></svg></i>EMAIL: info@caldermindworks.example</span>
</div>
<div class="abs brand"><i class="brand-dot"></i>Calder Mindworks<br>Psychology</div>
<nav class="nav">
  <a class="active" style="left:486px">HOME</a>
  <a style="left:579px">Solutions</a>
  <a style="left:673px">About Us</a>
  <a style="left:766px">Giving Back</a>
  <a style="left:858px">Login</a>
</nav>
<i class="soc" style="left:909px"></i><i class="soc" style="left:948px"></i><i class="soc" style="left:986px"></i><i class="soc" style="left:1023px"></i>

<div class="abs hero-photo" role="img" aria-label="Therapist smiling and holding a sad face card and a happy face card"></div>
<svg class="abs" style="left:0;top:680px" width="1200" height="150" viewBox="0 0 1200 150">
  <path d="M0 40 Q400 150 1200 20 L1200 150 L0 150Z" fill="#fff"/>
  <path d="M0 45 Q420 160 1200 15 L1200 40 Q420 175 0 55Z" fill="var(--green)"/>
  <path d="M0 60 Q420 185 1200 50" fill="none" stroke="var(--green)" stroke-width="4"/>
</svg>
<div class="abs hero-tag">We are experts in</div>
<div class="abs hero-title head-font">Psychology</div>
<p class="abs hero-text">Lorem ipsum dolor sit amet, consectetur adipiscing elit, sed do eiusmod tempor incididunt ut labore et dolore magna aliqua.</p>
<div class="abs btn hero-btn">Read More</div>

<div class="abs about-photo" role="img" aria-label="Three business professionals shaking hands"></div>
<div class="abs label" style="left:610px;top:904px">Who we are</div>
<h2 class="abs h2" style="left:610px;top:936px;width:460px">New Perspective for a Better Life</h2>
<div class="abs head-font" style="left:610px;top:1053px;font-size:20px;font-weight:500;color:var(--navy)">Strengthening Minds, Healing Hearts</div>
<p class="abs p-small" style="left:610px;top:1092px;width:455px">Lorem ipsum dolor sit amet, consectetur adipiscing elit, sed do eiusmod temp or incididunt ut labore et dolore magna aliqua. Ut enim ad minim veniam, quis laboris nisi ut aliquip ex ea commodo consequat.</p>
<p class="abs p-small" style="left:610px;top:1160px;width:455px">Lorem ipsum dolor sit amet, consectetur adipiscing elit, sed do eiusmod temp or incididunt ut labore et dolore magna aliqua.</p>
<div class="abs btn" style="left:610px;top:1224px;width:136px;height:40px;font-size:14px">Contact us <svg width="16" height="12" viewBox="0 0 16 12"><path d="M0 6h14M9 1l5 5-5 5" fill="none" stroke="#fff" stroke-width="1.6"/></svg></div>

<div class="abs services" role="img" aria-label="Counselling session in a softly lit room"></div>
<div class="abs label" style="left:552px;top:1398px;color:#fff;border-color:#fff">Our services</div>
<h2 class="abs head-font" style="left:0;width:1200px;text-align:center;top:1434px;color:#fff;font-size:42px;font-weight:500">Services We Provide</h2>
<div class="svc-card" style="left:164px;top:1538px;width:290px;height:267px">
  <div class="svc-icon"><svg width="40" height="40" viewBox="0 0 40 40"><circle cx="20" cy="20" r="15" fill="none" stroke="#fff" stroke-width="2"/><path d="M20 20l5-8" stroke="#fff" stroke-width="2"/></svg></div>
  <h3>Psychology Therapy</h3><p>Lorem ipsum dolor sit amet, con sectetur adipiscing elit, sed do eiusmod tem</p>
</div>
<div class="svc-card feature" style="left:454px;top:1520px;width:286px;height:301px;padding-top:44px">
  <div class="svc-icon"><svg width="40" height="40" viewBox="0 0 40 40"><path d="M20 6l13 10-5 16H12L7 16z" fill="none" stroke="var(--green)" stroke-width="2"/></svg></div>
  <h3>Clinical Supervision</h3><p>Lorem ipsum dolor sit amet, con sectetur adipiscing elit, sed do eiusmod tem</p>
</div>
<div class="svc-card" style="left:740px;top:1538px;width:284px;height:267px">
  <div class="svc-icon"><svg width="40" height="40" viewBox="0 0 40 40"><path d="M8 32h24M14 32l10-20 4 3-8 17" fill="none" stroke="#fff" stroke-width="2"/></svg></div>
  <h3>Training &amp; Consultancy</h3><p>Lorem ipsum dolor sit amet, con sectetur adipiscing elit, sed do eiusmod tem</p>
</div>

<div class="abs why-bg"></div>
<div class="abs why-photo" role="img" aria-label="Smiling professional woman holding a tablet"></div>
<div class="abs label" style="left:615px;top:1985px">Why choose us</div>
<h2 class="abs h2" style="left:615px;top:2025px;font-size:42px;line-height:50px">Healing Minds,<br>Transforming Lives</h2>
<div class="feat" style="left:602px;top:2151px"><svg width="32" height="32" viewBox="0 0 32 32"><path d="M4 28h24M10 28l8-17 4 3-6 14" fill="none" stroke="#4a5566" stroke-width="1.6"/></svg><h4>Confidentiality</h4><p>Inventore veritasis uas vitae dicta sunt</p></div>
<div class="feat" style="left:847px;top:2151px"><svg width="32" height="32" viewBox="0 0 32 32"><path d="M4 28h24M10 28l8-17 4 3-6 14" fill="none" stroke="#4a5566" stroke-width="1.6"/></svg><h4>Client-centric</h4><p>Inventore veritasis uas vitae dicta sunt</p></div>
<div class="feat" style="left:602px;top:2276px"><svg width="32" height="32" viewBox="0 0 32 32"><path d="M4 28h24M10 28l8-17 4 3-6 14" fill="none" stroke="#4a5566" stroke-width="1.6"/></svg><h4>Professionalism</h4><p>Inventore veritasis uas vitae dicta sunt</p></div>
<div class="feat" style="left:847px;top:2276px"><svg width="32" height="32" viewBox="0 0 32 32"><path d="M4 28h24M10 28l8-17 4 3-6 14" fill="none" stroke="#4a5566" stroke-width="1.6"/></svg><h4>Proven Record</h4><p>Inventore veritasis uas vitae dicta sunt</p></div>

<div class="abs steps-bg"></div>

<div class="abs appt" role="img" aria-label="Dimly lit consultation background"></div>
<div class="abs appt-people" role="img" aria-label="Two smiling professionals in suits with arms crossed"></div>
<h2 class="abs head-font" style="left:130px;top:2614px;color:#fff;font-size:33px;font-weight:500">Request An Appointment</h2>
<div class="field" style="left:130px;top:2688px"><svg width="14" height="14" viewBox="0 0 14 14"><circle cx="7" cy="4" r="3" fill="none" stroke="#333"/><path d="M1 13c1-4 11-4 12 0" fill="none" stroke="#333"/></svg>Full Name</div>
<div class="field" style="left:389px;top:2688px"><svg width="14" height="14" viewBox="0 0 14 14"><rect x="1" y="2" width="12" height="10" fill="none" stroke="#333"/></svg>Email Address</div>
<div class="field" style="left:130px;top:2754px"><svg width="14" height="14" viewBox="0 0 24 24"><path d="M5 3l4 1 1 5-2 1a11 11 0 006 6l1-2 5 1 1 4-3 2C10 21 3 14 3 6z" fill="none" stroke="#333" stroke-width="1.6"/></svg>Phone</div>
<div class="field tall" style="left:389px;top:2754px"><svg width="14" height="14" viewBox="0 0 14 14"><rect x="1" y="3" width="12" height="8" fill="none" stroke="#333"/><path d="M1 3l6 5 6-5" fill="none" stroke="#333"/></svg>Message</div>
<div class="field" style="left:130px;top:2823px"><svg width="14" height="14" viewBox="0 0 14 14"><circle cx="7" cy="7" r="6" fill="none" stroke="#333"/><path d="M7 7l3-3" stroke="#333"/></svg>Date</div>
<div class="abs btn" style="left:130px;top:2885px;width:132px;height:39px;font-size:12.5px;font-family:'Open Sans',sans-serif;font-weight:400">Request Now <svg width="10" height="10" viewBox="0 0 10 10"><path d="M0 5h8M5 2l3 3-3 3" fill="none" stroke="#fff"/></svg></div>

<div class="abs label" style="left:549px;top:3156px">Steps to take</div>
<h2 class="abs h2" style="left:0;width:1200px;text-align:center;top:3195px;font-size:42px">Steps to Take</h2>
<div class="step" style="left:122px"><div class="step-icon"><svg width="44" height="44" viewBox="0 0 32 32"><path d="M4 28h24M10 28l8-17 4 3-6 14" fill="none" stroke="#fff" stroke-width="1.6"/></svg></div><span class="step-num">1</span><h4>Get in touch with us</h4><p>Lorem ipsum dolor sit amet, con sectetur adipiscing elit, sed do eiusmod tempor incididunt ut labore et dol ore magna aliqua. Ut</p><span class="more">Read More</span></div>
<div class="step feature" style="left:365px"><div class="step-icon"><svg width="44" height="44" viewBox="0 0 40 40"><path d="M20 6l13 10-5 16H12L7 16z" fill="none" stroke="var(--green)" stroke-width="2"/></svg></div><span class="step-num">2</span><h4>Speak to an Expert</h4><p>Lorem ipsum dolor sit amet, con sectetur adipiscing elit, sed do eiusmod tempor incididunt ut labore et dol ore magna aliqua. Ut</p><span class="more">Read More</span></div>
<div class="step" style="left:613px"><div class="step-icon"><svg width="44" height="44" viewBox="0 0 40 40"><circle cx="20" cy="20" r="15" fill="none" stroke="#fff" stroke-width="2"/><path d="M20 20l5-8" stroke="#fff" stroke-width="2"/></svg></div><span class="step-num">3</span><h4>Schedule a meeting</h4><p>Lorem ipsum dolor sit amet, con sectetur adipiscing elit, sed do eiusmod tempor incididunt ut labore et dol ore magna aliqua. Ut</p><span class="more">Read More</span></div>
<div class="step" style="left:858px"><div class="step-icon"><svg width="44" height="44" viewBox="0 0 40 40"><circle cx="20" cy="20" r="14" fill="none" stroke="#fff" stroke-width="2"/><circle cx="26" cy="26" r="5" fill="none" stroke="#fff" stroke-width="2"/></svg></div><span class="step-num">4</span><h4>Start Sessions</h4><p>Lorem ipsum dolor sit amet, con sectetur adipiscing elit, sed do eiusmod tempor incididunt ut labore et dol ore magna aliqua. Ut</p><span class="more">Read More</span></div>

<div class="abs footer"></div>
<svg class="abs" style="left:0;top:3680px" width="1200" height="140" viewBox="0 0 1200 140">
  <path d="M0 90 Q600 -40 1200 110 L1200 140 L0 140Z" fill="var(--footer)"/>
  <path d="M0 90 Q600 -40 1200 110 L1200 90 Q600 -60 0 70Z" fill="var(--green)"/>
</svg>
<div class="abs head-font" style="left:0;width:1200px;top:3855px;text-align:center;color:#fff;font-size:34px;font-weight:500">Calder Mindworks Psychology</div>
<nav class="foot-nav">
  <a style="left:296px">HOME</a><a style="left:390px">SERVICES</a><a style="left:496px">ABOUT US</a><a style="left:614px">TESTIMONIALS</a><a style="left:764px">BLOG</a>
</nav>
<div class="abs" style="left:141px;top:4000px;width:918px;height:1px;background:#4a5270"></div>
<div class="abs" style="left:398px;top:4030px;width:1px;height:62px;background:#4a5270"></div>
<div class="abs" style="left:717px;top:4030px;width:1px;height:62px;background:#4a5270"></div>
<div class="contact" style="left:141px"><i class="c-ring"><svg width="30" height="30" viewBox="0 0 30 30"><circle cx="15" cy="15" r="11" fill="none" stroke="#fff" stroke-width="1.5"/><path d="M4 15h22M15 4v22" stroke="#fff" stroke-width="1.5"/></svg></i><span>48 Alder Grove Lane,<br>Brookhaven, ST 55012</span></div>
<div class="contact" style="left:474px"><i class="c-ring"><svg width="24" height="30" viewBox="0 0 24 30"><rect x="5" y="3" width="14" height="24" rx="2" fill="none" stroke="#fff" stroke-width="1.5"/></svg></i><span>PHONE<br>(555) 014 2290</span></div>
<div class="contact" style="left:796px"><i class="c-ring"><svg width="30" height="30" viewBox="0 0 30 30"><rect x="4" y="9" width="22" height="15" fill="none" stroke="#fff" stroke-width="1.5"/><path d="M4 9l11 9 11-9" fill="none" stroke="#fff" stroke-width="1.5"/></svg></i><span>EMAIL<br>info@caldermindworks.example</span></div>
<div class="abs bottom"><span style="position:absolute;left:146px;top:19px">Calder Mindworks Psychology</span>
  <i class="sq" style="left:933px"></i><i class="sq" style="left:966px"></i><i class="sq" style="left:999px"></i><i class="sq" style="left:1032px"></i>
</div>

</body>
</html>
```